business card for an electronic retail store

take our existing color logo, design a new business card and make a black&white version of the logo as well

Industry/Entity Type

Electronic

```html
<!DOCTYPE html>
<html lang="en">
<head>
<meta charset="utf-8">
<title>Voltwerk Business Card</title>
<link href="https://fonts.googleapis.com/css2?family=Montserrat:wght@400;500;600;800&display=swap" rel="stylesheet">
<style>
  :root {
    --bg: #d9d9d9;
    --card-black: #111111;
    --brand-yellow: #f7d200;
    --brand-red: #d0121b;
    --text-light: #e8e8e8;
    --text-muted: #b5b5b5;
    --ink: #111111;
  }
  * { margin: 0; padding: 0; box-sizing: border-box; }
  html, body { width: 1200px; height: 899px; overflow: hidden; }
  body {
    background: var(--bg);
    font-family: "Montserrat", Arial, sans-serif;
    display: flex;
    align-items: center;
    justify-content: center;
    gap: 60px;
  }
  .card {
    position: relative;
    width: 525px;
    height: 300px;
    background: var(--card-black);
    border-radius: 34px 8px 34px 8px;
    overflow: hidden;
    box-shadow: 0 10px 30px rgba(0,0,0,.25);
  }
  .logo {
    display: flex;
    align-items: center;
    gap: 8px;
  }
  .logo-mark {
    width: 18px;
    height: 18px;
    background: var(--brand-red);
  }
  .logo-name {
    font-weight: 800;
    color: var(--brand-yellow);
    letter-spacing: 1px;
  }
  .tagline {
    color: var(--brand-yellow);
    font-size: 11px;
    font-weight: 500;
    margin-top: 6px;
  }

  /* Front */
  .front .brand { position: absolute; left: 36px; top: 92px; }
  .front .logo-name { font-size: 34px; }
  .front-wave { position: absolute; left: 0; bottom: 0; width: 525px; height: 150px; }
  .front .website {
    position: absolute;
    right: 30px;
    bottom: 20px;
    font-size: 12px;
    font-weight: 600;
    letter-spacing: 1.5px;
    color: var(--ink);
  }

  /* Back */
  .back .brand { position: absolute; right: 40px; top: 26px; }
  .back .logo-mark { width: 14px; height: 14px; }
  .back .logo-name { font-size: 24px; }
  .back .tagline { font-size: 9px; text-align: right; margin-top: 3px; }
  .person { position: absolute; left: 150px; top: 92px; }
  .person-name { color: var(--text-light); font-size: 15px; font-weight: 500; letter-spacing: 1px; text-transform: uppercase; }
  .person-title { color: var(--text-muted); font-size: 10px; margin-top: 2px; }
  .address { color: var(--text-light); font-size: 11px; line-height: 1.4; margin-top: 16px; }
  .contacts { list-style: none; margin-top: 16px; }
  .contacts li {
    display: flex; align-items: center; gap: 8px;
    color: var(--text-muted); font-size: 10px; margin-bottom: 7px;
  }
  .contacts svg { width: 11px; height: 11px; fill: var(--text-muted); }
  .back-stripe { position: absolute; left: 0; top: 0; width: 525px; height: 12px; }
</style>
</head>
<body>

  <section class="card front">
    <div class="brand">
      <div class="logo"><span class="logo-mark"></span><span class="logo-name">VOLTWERK</span></div>
      <p class="tagline">Car Audio • Performance • Security</p>
    </div>
    <svg class="front-wave" viewBox="0 0 525 150" preserveAspectRatio="none">
      <path d="M0 20 C120 60 200 95 300 95 C400 95 470 70 525 50 L525 150 L0 150 Z" fill="var(--brand-red)"/>
      <path d="M0 32 C120 72 200 108 300 108 C400 108 470 82 525 62 L525 150 L0 150 Z" fill="var(--card-black)"/>
      <path d="M0 40 C120 80 200 118 300 118 C400 118 470 90 525 70 L525 150 L0 150 Z" fill="var(--brand-yellow)"/>
    </svg>
    <p class="website">www.voltwerkaudio.com</p>
  </section>

  <section class="card back">
    <div class="brand">
      <div class="logo"><span class="logo-mark"></span><span class="logo-name">VOLTWERK</span></div>
      <p class="tagline">Car Audio • Performance • Security</p>
    </div>
    <div class="person">
      <p class="person-name">Marcus Hale</p>
      <p class="person-title">Managing Director</p>
      <p class="address">21 Harbor Plaza Lvl 4<br>Ridgeway Road</p>
      <ul class="contacts">
        <li><svg viewBox="0 0 12 12"><path d="M3 0h2l1 3-1.5 1a7 7 0 0 0 3.5 3.5L9 6l3 1v2c0 1-1 3-3 3C4 12 0 8 0 3 0 1 2 0 3 0z"/></svg>012 555 0199</li>
        <li><svg viewBox="0 0 12 12"><path d="M3 0h6a1 1 0 0 1 1 1v10a1 1 0 0 1-1 1H3a1 1 0 0 1-1-1V1a1 1 0 0 1 1-1zm0 2v7h6V2z"/></svg>012 555 0199</li>
        <li><svg viewBox="0 0 12 12"><path d="M2 4h8V1H2zM0 5h12v5H9v2H3v-2H0z"/></svg>012 555 0199</li>
        <li><svg viewBox="0 0 12 12"><path d="M0 2h12v8H0zm1 1v.5l5 3 5-3V3z"/></svg>hello@voltwerk.com</li>
        <li><svg viewBox="0 0 12 12"><circle cx="6" cy="6" r="6"/></svg>www.voltwerkaudio.com</li>
      </ul>
    </div>
  </section>

</body>
</html>
```